Web Page for marketing online agency

We are an online marketing agency that is acing the direct response model. We engage with our customers throughout different marketing techniques as research copy-writing, advertisements and content writing. We would need a website design that will have four main aspects: The Vision; stating who we are, The Mission; stating what we do, The Team And It's Values, and a Contact Form. For this design we would want a sharp, clean and smart approach, with illustrated elements or suggestive images. You can use the attached copy, the logo, the USP and the motto. Please integrate them as you see fit while keeping in mind the previous needs and copy. This website is going to be our connection with our possible partners, future colleagues and even our clients. You may submit a design for one page or integrate the 4 different aspects on separate web pages.
Target Market(s)
business partners, future employees, age range 25-60
Industry/Entity Type
Direct Marketing
Number of Pages Required
1 page
Requirements
Must have
- Menu / Header
- 4 Parts or 4 Pages including: vision, mission, team, contact
- Logo
- Motto: Direct Brilliance
- USP: We help people help themselves.
- The copy attached
Nice to have
- Representative illustrated images or elements
Should not have
- A boring design, classical design - Pagequill like

```html
<!DOCTYPE html>
<html lang="en">
<head>
<meta charset="utf-8">
<title>VaroBros – Direct Brilliance</title>
<link href="https://fonts.googleapis.com/css2?family=Quicksand:wght@300;400;500;600;700&display=swap" rel="stylesheet">
<style>
:root{
  --blue:#2f9fe0;
  --blue-dark:#1a7fc4;
  --ink:#222428;
  --text:#555a60;
  --muted:#9aa0a6;
  --white:#ffffff;
  --mission:#2b2c2e;
  --team:#18262a;
  --footer:#141516;
}
*{margin:0;padding:0;box-sizing:border-box}
html,body{width:1200px;height:3422px;overflow:hidden}
body{font-family:"Quicksand",sans-serif;color:var(--text);background:var(--white);position:relative}
.abs{position:absolute}
.wave{position:absolute;left:0;width:1200px;height:70px}
.chev{position:absolute;left:584px;width:32px;height:20px}

/* header */
.hero{top:0;left:0;width:1200px;height:684px;background:linear-gradient(180deg,#cfd6dd 0%,#e4e7ea 55%,#ece6d4 100%)}
.hero-art{position:absolute;left:0;top:110px;width:1200px;height:574px;background:linear-gradient(180deg,rgba(140,160,180,.25),rgba(120,150,170,.35) 60%,rgba(200,185,150,.45))}
.brand{position:absolute;left:78px;top:44px;font-size:40px;font-weight:600;color:var(--ink);letter-spacing:.5px}
.nav{position:absolute;top:46px;left:382px;display:flex;font-size:15px}
.nav a{color:#4a4f55;text-decoration:none;margin-right:32px}
.nav a.active{color:var(--ink);font-weight:600;position:relative}
.nav a.active::before{content:"";position:absolute;left:12px;top:-22px;width:16px;height:16px;border-radius:50%;background:var(--blue)}
.signin{position:absolute;left:1020px;top:36px;width:104px;height:40px;border-radius:20px;background:var(--blue);color:#fff;font-size:14px;font-weight:700;display:flex;align-items:center;justify-content:center;gap:6px;box-shadow:0 3px 0 var(--blue-dark)}

h2{font-weight:400;color:var(--ink);text-align:center;font-size:38px}
h2 .hl{color:var(--blue)}

/* who */
.who{top:684px;left:0;width:1200px;height:593px;background:var(--white)}
.who h2{position:absolute;top:40px;width:1200px}
.who .lead{position:absolute;top:112px;left:150px;width:900px;text-align:center;font-size:15px;line-height:1.75}
.who ul{position:absolute;list-style:none;font-size:12px;line-height:1.6;color:var(--muted)}
.who li{position:relative;padding-left:24px;margin-bottom:12px}
.who li::before{content:"";position:absolute;left:2px;top:7px;width:6px;height:6px;border-radius:50%;background:#c8cdd2}
.who b{color:#444;font-weight:600}
.col-l{top:230px;left:88px;width:480px}
.col-r{top:212px;left:605px;width:510px}

/* mission */
.mission{top:1277px;left:0;width:1200px;height:411px;background:var(--mission)}
.mission-art{position:absolute;inset:0;background:radial-gradient(ellipse at 70% 40%,rgba(80,82,86,.6),rgba(43,44,46,0) 60%)}
.mission h2{position:absolute;top:70px;width:1200px;color:#fff}
.mission .copy{position:absolute;top:136px;left:130px;width:940px;text-align:center;color:#d8dadc;font-size:14px;line-height:1.8}
.mission .copy p{margin-bottom:12px}

/* values */
.values{top:1688px;left:0;width:1200px;height:376px;background:var(--white)}
.values h2{position:absolute;top:50px;width:1200px}
.value{position:absolute;top:118px;width:190px;text-align:center}
.value svg{width:56px;height:56px}
.value h3{font-weight:500;font-size:17px;color:var(--blue);margin-top:6px}
.value.dark h3{color:var(--ink)}
.value p{font-size:12px;color:var(--muted);line-height:1.55;margin-top:8px}

/* team */
.team{top:2064px;left:0;width:1200px;height:422px;background:var(--team)}
.team-art{position:absolute;inset:0;background:linear-gradient(90deg,rgba(40,60,64,.5),rgba(24,38,42,0) 50%,rgba(40,60,64,.5))}
.team h2{position:absolute;top:80px;width:1200px;color:#fff}
.team .intro{position:absolute;top:144px;left:120px;width:960px;text-align:center;color:#d6dbdd;font-size:14px;line-height:1.65}
.card{position:absolute;top:213px;width:506px;height:132px;background:rgba(110,125,128,.45);border:1px solid rgba(255,255,255,.15);padding:18px 20px 0 104px;color:#d9dee0;font-size:12px;line-height:1.55}
.avatar{position:absolute;left:20px;top:18px;width:60px;height:56px;background:linear-gradient(135deg,#8b9497,#5e686b)}
.card .name{font-size:15px;color:var(--blue);margin-bottom:6px}
.card .role{font-size:11px;color:#b9c1c4;margin-left:8px}
.card .more{position:absolute;right:22px;bottom:20px;font-size:12px;text-decoration:underline;color:#fff}

/* direct response */
.direct{top:2486px;left:0;width:1200px;height:336px;background:var(--white)}
.direct-art{position:absolute;left:430px;top:0;width:770px;height:336px;background:linear-gradient(90deg,rgba(235,237,239,0),rgba(218,222,226,.8) 30%,rgba(225,228,231,.9))}
.direct h2{position:absolute;top:52px;width:1200px}
.direct .left{position:absolute;top:106px;left:80px;width:440px;color:var(--ink);font-size:15px;font-weight:600;line-height:1.55}
.direct ol{list-style:none;margin-top:14px;font-weight:400;font-size:12px;color:var(--text);padding-left:24px}
.direct ol li{margin-bottom:10px}
.direct .right{position:absolute;top:168px;left:604px;width:440px;color:var(--ink);font-size:15px;font-weight:600;line-height:1.55}

/* contact */
.contact{top:2822px;left:0;width:1200px;height:458px;background:linear-gradient(180deg,#6f8da6,#3e5f78 60%,#2f4b5e)}
.contact h2{position:absolute;top:52px;width:1200px;color:#fff}
.field{position:absolute;left:80px;width:578px;background:#fff;border-radius:14px;font-size:12px;color:#a6acb2;padding:12px 24px}
.f1{top:120px;height:44px}.f2{top:176px;height:44px}.f3{top:232px;height:80px}
.submit{position:absolute;left:80px;top:328px;width:578px;height:44px;border-radius:22px;background:var(--blue);color:#0f2a3c;font-weight:700;font-size:16px;display:flex;align-items:center;justify-content:center;box-shadow:0 3px 0 #1b5d86}
.info{position:absolute;left:722px;color:#fff;font-size:15px}
.info svg{position:absolute;left:0;top:2px}
.info .t{position:absolute;left:42px;white-space:nowrap}
.info .sub{color:#d7e1ea;font-size:13px;line-height:1.55}

/* footer */
.footer{top:3280px;left:0;width:1200px;height:142px;background:var(--footer)}
.footer .brand-f{position:absolute;top:42px;width:1200px;text-align:center;font-size:32px;font-weight:600;color:#fff}
.footer .copy{position:absolute;top:102px;width:1200px;text-align:center;color:#cfd2d5;font-size:12px}
</style>
</head>
<body>

<header class="abs hero">
  <div class="hero-art" role="img" aria-label="Illustrated city of smartphones and tablets with people climbing screens and working on clouds"></div>
  <div class="brand">VaroBros</div>
  <nav class="nav">
    <a class="active" href="#">Home</a>
    <a href="#">About Us</a>
    <a href="#">What We Do</a>
    <a href="#">Marketing</a>
    <a href="#">Team &amp; Values</a>
    <a href="#">Contact Us</a>
  </nav>
  <div class="signin">
    <svg width="14" height="14" viewBox="0 0 14 14"><circle cx="7" cy="7" r="6" fill="none" stroke="#fff" stroke-width="1.6"/><path d="M5 4l3 3-3 3" fill="none" stroke="#fff" stroke-width="1.6"/></svg>
    SIGN-IN
  </div>
</header>

<section class="abs who">
  <svg class="wave" style="top:-36px" viewBox="0 0 1200 70" preserveAspectRatio="none"><path d="M0 36 H470 C540 36 540 0 600 0 C660 0 660 36 730 36 H1200 V70 H0Z" fill="#fff"/></svg>
  <svg class="chev" style="top:-26px" viewBox="0 0 32 20"><path d="M6 5l10 10 10-10" fill="none" stroke="#9aa0a6" stroke-width="2.5"/></svg>
  <h2>Who we <span class="hl">are?</span></h2>
  <div class="lead">
    <p>We are a direct response company that creates and sells information products and services that millions of people find interesting and important in their lives.</p>
    <p style="margin-top:10px">We are specialized in the self-reliance market and we serve conservative Americans.</p>
  </div>
  <ul class="col-l">
    <li>We are in this business to serve globally and to grow individually.</li>
    <li>What we serve and inspire are people who need safety, comfort and peace of mind.</li>
    <li>We deliver <b>empowerment</b> through products that create fertile <b>shortcuts</b> to solutions, <b>disentangle</b> reality, <b>simplify</b> choices and ultimately <b>make lives better.</b></li>
    <li>We give <b>reassurance</b> and <b>confidence</b> to these people through fresh, unique solutions.</li>
    <li>We invest time and energy in becoming better <b>in the competition with ourselves.</b></li>
  </ul>
  <ul class="col-r">
    <li>We get our <b>inspiration</b> from <b>modern heroes</b> and make their stories available for others.</li>
    <li>In a way we are <b>democratizing wisdom</b> because we solve serious problems shared by millions of people worldwide.</li>
    <li>We might not directly save lives, but we try to make a change. We help people help themselves.</li>
    <li>With our thirst for knowledge and drive for constant improvement, we know we'll find a solution to any challenge.</li>
    <li>And while doing that, we decided to <b>water our inner seeds and harvest the best of our humanity.</b></li>
    <li>We believe that our better selves of tomorrow will nurture better tomorrows for others.</li>
  </ul>
</section>

<section class="abs mission">
  <div class="mission-art" role="img" aria-label="Dark photo of a desk with notes, pens and paper clips"></div>
  <svg class="wave" style="top:-36px" viewBox="0 0 1200 70" preserveAspectRatio="none"><path d="M0 36 H470 C540 36 540 0 600 0 C660 0 660 36 730 36 H1200 V70 H0Z" fill="#2b2c2e"/></svg>
  <svg class="chev" style="top:-26px" viewBox="0 0 32 20"><path d="M6 5l10 10 10-10" fill="none" stroke="#fff" stroke-width="2.5"/></svg>
  <h2>What We Do? Our Mission</h2>
  <div class="copy">
    <p>It's our passion, our way of life, and it's our biggest source of accomplishment and frustration at the same time. It's a "beast" that's constantly changing and evolving. And we're changing and evolving with it, to stay at the top of the game.</p>
    <p>In direct response you sell or else, as they say. It's true to a point. It's true we are good at selling. But being a good seller is a matter of being relevant first and foremost, fresh, timely and intriguing.<br>If we were not helping people in tangible ways, they wouldn't reward us with their trust. We love to help and inspire people.<br>For us selling well means doing good.</p>
  </div>
</section>

<section class="abs values">
  <svg class="wave" style="top:-36px" viewBox="0 0 1200 70" preserveAspectRatio="none"><path d="M0 36 H470 C540 36 540 0 600 0 C660 0 660 36 730 36 H1200 V70 H0Z" fill="#fff"/></svg>
  <svg class="chev" style="top:-26px" viewBox="0 0 32 20"><path d="M6 5l10 10 10-10" fill="none" stroke="#9aa0a6" stroke-width="2.5"/></svg>
  <h2>Our <span class="hl">Values</span></h2>
  <div class="value" style="left:87px">
    <svg viewBox="0 0 56 56"><g fill="none" stroke="#8a9096" stroke-width="2"><path d="M28 8v40M14 48h28M10 16h36"/><path d="M10 16l-6 14h12zM46 16l-6 14h12z"/></g></svg>
    <h3>Fairness</h3><p>We are in this business to serve globally and to grow individually.</p>
  </div>
  <div class="value" style="left:295px">
    <svg viewBox="0 0 56 56"><g fill="#8a9096"><circle cx="28" cy="20" r="9"/><path d="M6 36c8-4 16-2 22 2h14c4 0 4 6 0 6H22v2h22l8-8v8L44 52H6z"/></g></svg>
    <h3>Caring</h3><p>We are in this business to serve globally and to grow individually.</p>
  </div>
  <div class="value dark" style="left:503px">
    <svg viewBox="0 0 56 56"><path d="M28 4l20 8v14c0 14-9 22-20 26C17 48 8 40 8 26V12z" fill="none" stroke="var(--blue)" stroke-width="3"/><path d="M19 28l7 7 12-13" fill="none" stroke="var(--blue)" stroke-width="3.5"/></svg>
    <h3>Safety</h3><p>We are in this business to serve globally and to grow individually.</p>
  </div>
  <div class="value" style="left:712px">
    <svg viewBox="0 0 56 56"><g fill="none" stroke="#8a9096" stroke-width="2"><path d="M24 8h8v6h-8zM22 14h12l-2 30H24zM18 44h20v6H18zM20 24h16"/></g></svg>
    <h3>Freedom</h3><p>We are in this business to serve globally and to grow individually.</p>
  </div>
  <div class="value" style="left:922px">
    <svg viewBox="0 0 56 56"><path d="M18 18c0-14 22-14 22 0 0 10-10 10-10 20" fill="none" stroke="#8a9096" stroke-width="5"/><circle cx="30" cy="48" r="3.5" fill="#8a9096"/></svg>
    <h3>Unconditioned help</h3><p>We are in this business to serve globally and to grow individually.</p>
  </div>
</section>

<section class="abs team">
  <div class="team-art" role="img" aria-label="Dark photo of an office workspace"></div>
  <svg class="wave" style="top:-36px" viewBox="0 0 1200 70" preserveAspectRatio="none"><path d="M0 36 H470 C540 36 540 0 600 0 C660 0 660 36 730 36 H1200 V70 H0Z" fill="#18262a"/></svg>
  <svg class="chev" style="top:-26px" viewBox="0 0 32 20"><path d="M6 5l10 10 10-10" fill="none" stroke="#fff" stroke-width="2.5"/></svg>
  <h2>Our Team</h2>
  <p class="intro">We're a small team of smart, funny hard-working specialists who are pushing to become the #1 company in self-reliance. High ambition, radical honesty and a result-oriented mindset are encouraged at VaroBros.</p>
  <div class="card" style="left:80px">
    <div class="avatar" role="img" aria-label="Portrait of Dorian Mare"></div>
    <div class="name">- Dorian Mare <span class="role">CEO VaroBros</span></div>
    <p>Dorian started or was involved in 15 failed businesses before discovering online copywriting. After that, he ended up writing for Norvex Inc.</p>
    <span class="more">READ MORE</span>
  </div>
  <div class="card" style="left:614px">
    <div class="avatar" role="img" aria-label="Portrait of Matei Corbu"></div>
    <div class="name">- Matei Corbu <span class="role">Cofounder &amp; Affiliate Manager</span></div>
    <p>Since the company's late 2012 start, Matei grew a network of 5000 affiliates, that dominates Tradehive's survival niche – 3 out of top 5 products are VaroBros offers...</p>
    <span class="more">READ MORE</span>
  </div>
</section>

<section class="abs direct">
  <div class="direct-art" role="img" aria-label="Faded photo of a group of business people standing together"></div>
  <svg class="wave" style="top:-36px" viewBox="0 0 1200 70" preserveAspectRatio="none"><path d="M0 36 H470 C540 36 540 0 600 0 C660 0 660 36 730 36 H1200 V70 H0Z" fill="#fff"/></svg>
  <svg class="chev" style="top:-26px" viewBox="0 0 32 20"><path d="M6 5l10 10 10-10" fill="none" stroke="#9aa0a6" stroke-width="2.5"/></svg>
  <h2>We live and breathe <span class="hl">direct response marketing.</span></h2>
  <div class="left">i. We are masters of direct response marketing. Our expertise is three folded:
    <ol>
      <li>1. We create and aggregate great information products.</li>
      <li>2. We write content that compels people to act.</li>
      <li>3. We do deep research to offer simple quick and easy solutions to people's most serious problems.</li>
    </ol>
  </div>
  <div class="right">ii. We create content and build solutions to profound challenges for millions of people</div>
</section>

<section class="abs contact">
  <svg class="wave" style="top:-36px" viewBox="0 0 1200 70" preserveAspectRatio="none"><path d="M0 36 H470 C540 36 540 0 600 0 C660 0 660 36 730 36 H1200 V70 H0Z" fill="#6f8da6"/></svg>
  <svg class="chev" style="top:-26px" viewBox="0 0 32 20"><path d="M6 5l10 10 10-10" fill="none" stroke="#222" stroke-width="2.5"/></svg>
  <h2 style="color:#fff">Contact Us</h2>
  <div class="field f1">Enter Name</div>
  <div class="field f2">Enter Email</div>
  <div class="field f3">Message</div>
  <div class="submit">SUBMIT</div>
  <div class="info" style="top:172px">
    <svg width="24" height="24" viewBox="0 0 24 24"><path d="M11 2v20M4 5h15l3 3-3 3H4zM20 13H6l-3 3 3 3h14z" fill="#fff"/></svg>
    <div class="t" style="font-size:20px;top:-2px">Varo Bros</div>
    <div class="t sub" style="top:36px">Strada Teilor 24,<br>Bucuresti 011042</div>
  </div>
  <div class="info" style="top:266px">
    <svg width="22" height="22" viewBox="0 0 24 24"><path d="M6 2l4 5-2 3c1 3 3 5 6 6l3-2 5 4-3 4C10 22 2 14 2 5z" fill="#fff"/></svg>
    <div class="t" style="top:0">123 555 0199</div>
  </div>
  <div class="info" style="top:308px">
    <svg width="22" height="18" viewBox="0 0 22 18"><rect x="1" y="1" width="20" height="16" fill="#fff"/><path d="M1 1l10 9 10-9" fill="none" stroke="#3e5f78" stroke-width="1.6"/></svg>
    <div class="t" style="top:-2px;text-decoration:underline">info@varobros.com</div>
  </div>
</section>

<footer class="abs footer">
  <svg class="wave" style="top:-36px" viewBox="0 0 1200 70" preserveAspectRatio="none"><path d="M0 36 H470 C540 36 540 0 600 0 C660 0 660 36 730 36 H1200 V70 H0Z" fill="#141516"/></svg>
  <svg class="chev" style="top:-24px" viewBox="0 0 32 20"><path d="M6 15l10-10 10 10" fill="none" stroke="#fff" stroke-width="2.5"/></svg>
  <div class="brand-f">VaroBros</div>
  <div class="copy">© <b>Varo Bros</b> – 2018. All Rights Reserved.</div>
</footer>

</body>
</html>
```